Billboard design 8x3M NURA (Spanish company)

We´re located in the south of Spain. We run a local telecom company.
We sell Fiber optic, and mobile phone lines mainly.
The billboard will have to be in Spanish, I would like the price to be something you spot on first sight when passing by in the car.
Our company color is blue, like in our logo which I will add. I will also add a example from what we currently have.
The new offer should be:
1000 megas + 100Gigas movil con llamadas ilimitadas. (meaning 1000Mb fiber optic speed and 100Gb data and unlimited calls for 1 mobile line)
Our details are: phone line 952 00 0147
Website: nu-ra.es

```html
<!DOCTYPE html>
<html lang="es">
<head>
<meta charset="utf-8">
<title>NURA – Valla 8x3</title>
<link rel="stylesheet" href="https://fonts.googleapis.com/css2?family=Poppins:wght@500;600;700;800&display=swap">
<style>
  :root {
    --page: #e8ecf0;
    --blue-light: #2aa8e2;
    --blue-mid: #2387b8;
    --blue-deep: #1d5f80;
    --navy: #1a4257;
    --yellow: #ffec00;
    --white: #ffffff;
    --art-sky: #2fa9e6;
    --art-fire: #f07a1c;
  }
  * { margin: 0; padding: 0; box-sizing: border-box; }
  html, body {
    width: 1200px; height: 780px; overflow: hidden;
    background: var(--page);
    font-family: "Poppins", sans-serif;
  }
  .billboard {
    position: absolute; left: 40px; top: 180px;
    width: 1120px; height: 420px; overflow: hidden;
    background: linear-gradient(200deg, var(--blue-deep) 0%, var(--blue-mid) 55%, var(--blue-light) 100%);
    color: var(--white);
  }
  .brand { position: absolute; left: 40px; top: 56px; }
  .brand-name { font-size: 66px; font-weight: 800; line-height: 1; letter-spacing: 2px; }
  .brand-services { font-size: 16px; font-weight: 600; margin-top: 6px; }
  .pointer { position: absolute; left: 150px; top: 150px; width: 150px; height: 70px; }
  .price-label { position: absolute; left: 50px; top: 196px; font-size: 30px; font-weight: 600; }
  .price { position: absolute; left: 44px; top: 218px; font-size: 96px; font-weight: 800; color: var(--yellow); line-height: 1.1; letter-spacing: -3px; }
  .contact {
    position: absolute; left: 0; top: 322px; width: 262px; height: 84px;
    background: var(--navy); border-radius: 0 16px 16px 0;
    display: flex; flex-direction: column; justify-content: center; align-items: center;
    font-size: 25px; font-weight: 700; line-height: 1.2;
  }
  .offer { position: absolute; left: 282px; top: 22px; width: 380px; text-align: center; }
  .speed { font-size: 148px; font-weight: 800; color: var(--yellow); line-height: 1; letter-spacing: -5px; }
  .speed-unit {
    display: inline-block; margin-top: 4px; padding: 2px 34px;
    background: var(--navy); border-radius: 12px;
    font-size: 54px; font-weight: 700; line-height: 1.2; letter-spacing: 1px;
  }
  .data { font-size: 84px; font-weight: 800; color: var(--yellow); line-height: 1.05; letter-spacing: -2px; }
  .data-detail { font-size: 30px; font-weight: 600; line-height: 1.2; }
  .hero { position: absolute; left: 690px; top: 5px; width: 410px; height: 410px; }
</style>
</head>
<body>
  <main class="billboard">
    <div class="brand">
      <div class="brand-name">NURA</div>
      <div class="brand-services">Wifi | Fibra | Movil | Tv</div>
    </div>

    <svg class="pointer" viewBox="0 0 150 70" aria-hidden="true">
      <path d="M145 20 C 110 0, 60 2, 30 40" fill="none" stroke="#000" stroke-width="4"/>
      <path d="M18 56 L24 28 L44 44 Z" fill="#000"/>
    </svg>

    <div class="price-label">por</div>
    <div class="price">35€</div>

    <div class="contact">
      <span>952 00 0147</span>
      <span>www.nu-ra.es</span>
    </div>

    <div class="offer">
      <div class="speed">1000</div>
      <div class="speed-unit">MEGAS</div>
      <div class="data">+ 100Gb</div>
      <div class="data-detail">movil con llamadas<br>ilimitadas</div>
    </div>

    <svg class="hero" viewBox="0 0 410 410">
      <defs>
        <linearGradient id="launch" x1="0" y1="0" x2="1" y2="1">
          <stop offset="0.35" stop-color="var(--art-sky)"/>
          <stop offset="1" stop-color="var(--art-fire)"/>
        </linearGradient>
      </defs>
      <circle cx="205" cy="205" r="203" fill="var(--white)"/>
      <circle cx="205" cy="205" r="190" fill="var(--navy)"/>
      <circle cx="205" cy="205" r="160" fill="url(#launch)" role="img" aria-label="Ilustración de un cohete despegando entre humo naranja"/>
    </svg>
  </main>
</body>
</html>
```